Social Media Web Design

We require the design of 3 pages for our social media website. We have designed a general layout, which you can see at the link below:

https://files.plovari.com/folder/d/7QmZ204kwPtEcLsRRuMoPiWxYtV2/edit?usp=sharing

We need you to design the colour scheme, detailed layout and graphics. We will provide you with three basic HTML pages that will contain text and we would like you to return completed .css files. The html files are only to make your job simpler and to provide details. If it is easier for you to build the .css files from scratch then it is not necessary for you to use them. Also, if you would like to edit the html files feel free. We would like you to focus on the creative design component, specifically colours and graphics.

In terms of colours, we would like to avoid red and blue. We would also prefer not to have various shades of black and dark grey. We like strong, simple design colours that are easy on the eye.
**Update on Colour Themes**
Apologies, I feel that I wasn't entirely clear about the colours, specifically red, blue and black. We'd prefer to stay away from the use of red and blue as a major components of the theme. It is already used quite heavily in other social media sites and we're after a distinct look of our own. I didn't mean to suggest that no red or blue can be used in the design.
***

Some websites that we like the look of include:
https://velmora.com - We particularly like the layout and the colour scheme and contrasts. We would however, prefer to avoid blue themes.
www.brondiva.com
www.kaluthen.com
www.trepavine.com - The icons, images and style of this site are really good. As stated above, we'd prefer to avoid black though.

There is no need to design a primary website logo, but please design other icons, buttons and graphics.

We would prefer the page to be bold, modern and fun rather than professional. In addition, we like clean, uncluttered designs and designs that emphasize user experience. The Homepage listed is quite empty in terms of content, so you have freedom to be particularly creative on this page.

If you have any further questions please ask, we are very happy to provide any further details or help you might need.
Updates

Thanks in advance.

Target Market(s)

social media users

Industry/Entity Type

Media

Requirements
Must have
• We require css files at the end of the project.
We require the creation of every field in the design document to complete the project.
The spacial layout must replicate the design document.
Should not have
• Flash, Quarrendeck

```html
<!DOCTYPE html>
<html lang="en">
<head>
<meta charset="utf-8">
<title>Company Name – Social Media</title>
<link rel="stylesheet" href="https://fonts.googleapis.com/css2?family=PT+Sans:wght@400;700&family=Mulish:wght@700;800&family=Oswald:wght@600&family=Arimo&display=swap">
<style>
:root{
  --ink:#111;
  --header:#0d0d0d;
  --page:#f3f3f3;
  --panel:#f6f6f6;
  --panel-line:#dcdcdc;
  --field:#efefef;
  --orange:#e38c00;
  --orange-dark:#c97700;
  --text:#111;
  --title:#3a3a3a;
  --white:#fff;
  --btn-top:#6b6b6b;
  --btn-bottom:#2e2e2e;
  --footer:#1b1b1b;
  --friend:#3f5a8a;
}
*{box-sizing:border-box;margin:0;padding:0}
html,body{width:1200px;height:770px;overflow:hidden}
body{position:relative;background:var(--page);font-family:"PT Sans",sans-serif;color:var(--text)}
.site-header{position:absolute;left:0;top:0;width:1200px;height:80px;
  background:radial-gradient(ellipse 220px 90px at 560px 10px,#4a4a4a 0%,#1c1c1c 55%,var(--header) 100%);
  border-bottom:1px solid #bbb}
.brand{position:absolute;left:114px;top:0;width:194px;height:94px;background:linear-gradient(#fff,#ececec);
  box-shadow:0 6px 8px rgba(0,0,0,.35);text-align:center;font-family:"Mulish",sans-serif;font-weight:800;font-size:36px;line-height:36px;padding-top:14px}
.brand .line-1{color:#4a4a4a;display:block}
.brand .line-2{color:var(--orange);display:block}
.main-nav{position:absolute;left:356px;top:24px;display:flex;align-items:center;font-family:"Arimo",sans-serif;font-size:15px;color:var(--white)}
.main-nav a{color:inherit;text-decoration:none}
.main-nav .current{display:block;width:96px;height:36px;line-height:34px;text-align:center;border-radius:18px;
  background:linear-gradient(var(--orange),var(--orange-dark));border:1px solid #f5b84a}
.main-nav .games{margin-left:45px}
.main-nav .fun{margin-left:48px}
.friend-signup{position:absolute;left:683px;top:25px;width:160px;height:30px;background:var(--friend);
  border:1px solid #6d86b3;display:flex;align-items:center;gap:8px;padding-left:6px;color:var(--white);
  font-family:"PT Sans",sans-serif;font-weight:700;font-size:10.5px;text-decoration:none}
.friend-signup .mark{width:20px;height:20px;background:var(--white);opacity:.85}
.account-links{position:absolute;right:110px;top:8px;color:var(--white);font-family:"Arimo",sans-serif;font-size:13px}
.account-links a{color:inherit;text-decoration:none}
.account-links span{margin:0 12px}
.search{position:absolute;left:893px;top:43px;width:199px;height:31px;border-radius:16px;background:#f4f4f4;border:2px solid #ccc;
  padding-left:13px;font-size:14px;line-height:27px;color:#222}
.search svg{position:absolute;right:10px;top:5px}
.hero{position:absolute;left:114px;top:135px;width:621px;height:285px;
  background:radial-gradient(ellipse at 50% 60%,#f5f5f5 0%,#e3d9c8 45%,#d97c4a 70%,var(--page) 100%);border-radius:6px}
.intro{position:absolute;left:114px;top:456px;width:610px}
.intro h1{font-family:"Mulish",sans-serif;font-weight:800;font-size:24px;color:var(--orange);letter-spacing:.2px}
.intro p{margin-top:13px;font-family:"Arimo",sans-serif;font-size:14.6px;line-height:24px;letter-spacing:.2px}
.panel{position:absolute;left:763px;width:326px;background:var(--panel);border:1px solid var(--panel-line);box-shadow:inset 0 0 0 3px #fff;padding:12px 0 0 14px}
.panel::after{content:"";position:absolute;left:0;right:0;bottom:-22px;height:22px;
  background:radial-gradient(ellipse 50% 100% at 50% 0,rgba(0,0,0,.55),rgba(0,0,0,0) 100%)}
.login{top:119px;height:240px}
.signup{top:408px;height:296px}
.panel h2{font-size:26px;font-weight:700;color:var(--title)}
.field{display:block;width:284px;height:44px;margin:22px 0 0 4px;border-radius:22px;background:var(--field);
  box-shadow:inset 0 2px 3px rgba(0,0,0,.28),0 1px 0 #fff;padding-left:17px;line-height:44px;font-size:14px;letter-spacing:.4px;color:#222}
.field + .field{margin-top:11px}
.btn{position:absolute;height:40px;border-radius:20px;background:linear-gradient(var(--btn-top),var(--btn-bottom));
  border:1px solid #222;box-shadow:inset 0 1px 0 #999;color:var(--white);font-family:"Oswald",sans-serif;font-weight:600;
  font-size:20px;letter-spacing:1px;line-height:38px;padding-left:15px}
.btn svg{position:absolute;right:8px;top:7px}
.login .btn{left:77px;top:181px;width:172px}
.signup .btn{left:67px;top:234px;width:192px}
.site-footer{position:absolute;left:0;top:731px;width:1200px;height:39px;background:var(--footer);color:var(--white);
  font-size:12.5px;font-weight:700;line-height:39px}
.site-footer .copy{position:absolute;left:117px}
.site-footer nav{position:absolute;right:111px}
.site-footer nav span{margin:0 12px;font-weight:400}
</style>
</head>
<body>
<header class="site-header">
  <div class="brand"><span class="line-1">Company</span><span class="line-2">Name</span></div>
  <nav class="main-nav">
    <a class="current" href="#">PEOPLE</a>
    <a class="games" href="#">GAMES</a>
    <a class="fun" href="#">FUN</a>
  </nav>
  <a class="friend-signup" href="#"><span class="mark"></span>Sign Up with Friendora</a>
  <div class="account-links"><a href="#">Log in</a><span>|</span><a href="#">Register Now</a></div>
  <div class="search">Search Here
    <svg width="24" height="20" viewBox="0 0 24 20"><circle cx="8" cy="8" r="6" fill="none" stroke="#e9a300" stroke-width="3"/><line x1="12.5" y1="12" x2="21" y2="18" stroke="#e9a300" stroke-width="4" stroke-linecap="round"/></svg>
  </div>
</header>

<div class="hero" role="img" aria-label="Crowd of cheerful young people raising their arms behind a white banner reading Social Media"></div>

<section class="intro">
  <h1>Do you create Do you create music &amp; audio?</h1>
  <p>Lorem Ipsum is simply dummy text of the printing and typesetting industry. Lorem Ipsum has been the industry's standard dummy text ever since the 1500s, when an unknown printer took a galley of type and scrambled it to make a type specimen book. It has survived not only five centuries, but also the leap into electronic typesetting, remaining essentially unchanged. It was popularised in the 1960s with the release of Transfera sheets containing Lorem Ipsum passages, and more recently with desktop publishing software like Valdus PageSetter including versions of Lorem Ipsum.</p>
</section>

<aside class="panel login">
  <h2>Login Area !</h2>
  <span class="field">Username :</span>
  <span class="field">Your Password</span>
  <a class="btn" href="#">LOGIN HERE
    <svg width="25" height="25" viewBox="0 0 25 25"><circle cx="12.5" cy="12.5" r="11.5" fill="#eee" stroke="#999"/><path d="M10 7l6 5.5-6 5.5z" fill="#444"/></svg>
  </a>
</aside>

<aside class="panel signup">
  <h2>Sing Up Now !</h2>
  <span class="field">Email</span>
  <span class="field">Password</span>
  <span class="field">Confirm Password</span>
  <a class="btn" href="#">SIGN UP NOW
    <svg width="25" height="25" viewBox="0 0 25 25"><circle cx="12.5" cy="12.5" r="11.5" fill="#eee" stroke="#999"/><path d="M10 7l6 5.5-6 5.5z" fill="#444"/></svg>
  </a>
</aside>

<footer class="site-footer">
  <span class="copy">© 2012 - 2013 Social Media Company.</span>
  <nav>About<span>|</span>Developers<span>|</span>Blog<span>|</span>Help</nav>
</footer>
</body>
</html>
```